BRASKET LAND SERVICES BILLBOARD DESIGN

I NEED A BILLBOARD FOR MY BUSINESS. WE ARE A LAND CLEARING COMPANY AND I WOULD LIKE TO ADD A PICTURE OF MY TRACK LOADER TO THE SIGN. OPEN TO COLORS. I WOULD ALSO LIKE TO HAVE MY PHONE NUMBER 555-284-6170, WEBSITE WWW.BRASKETLANDSERVICES.EXAMPLE, AND EMAIL ON THE SIGN (CONTACT@BRASKETLANDSERVICES.EXAMPLE). DESIGNERS CAN HAVE THE FREEDOM TO DO WHATEVER STYLE THEY WANT AND TO USE ANY COLORS THEY WANT.

Target Market(s)

ANYONE WITH PROPERTY

Requirements
Must have
• PICTURE OF TRACK LOADER, WEBSITE, PHONE NUMBER, EMAIL
Nice to have
• OPEN TO ANYTHING
Should not have
• OPEN TO ANYTHING

```html
<!DOCTYPE html>
<html lang="en">
<head>
<meta charset="utf-8">
<title>Brasket Land Services Billboard</title>
<link rel="stylesheet" href="https://fonts.googleapis.com/css2?family=Alfa+Slab+One&family=Anton&family=Open+Sans:wght@600;700&display=swap">
<style>
  :root {
    --orange: #ee5526;
    --tan: #aca08a;
    --charcoal: #2b241f;
    --white: #ffffff;
    --ink: #1e1a17;
    --page: #ebebed;
  }
  * { margin: 0; padding: 0; box-sizing: border-box; }
  html, body {
    width: 977px;
    height: 1200px;
    overflow: hidden;
    background: var(--page);
  }
  .canvas {
    position: relative;
    width: 977px;
    height: 1200px;
  }
  .billboard {
    position: absolute;
    left: 18px;
    top: 463px;
    width: 1480px;
    height: 432px;
    transform: scale(0.635);
    transform-origin: 0 0;
    overflow: hidden;
    background: var(--orange);
  }
  .billboard-bg {
    position: absolute;
    inset: 0;
    width: 1480px;
    height: 432px;
  }
  .brand-name {
    position: absolute;
    left: 56px;
    top: 50px;
    font-family: "Alfa Slab One", "Rockwell", serif;
    font-weight: 400;
    font-size: 76px;
    line-height: 82px;
    color: var(--white);
    letter-spacing: 0.5px;
    white-space: nowrap;
    z-index: 2;
  }
  .loader-photo {
    position: absolute;
    left: 552px;
    top: 96px;
    width: 515px;
    height: 330px;
    border-radius: 40px 60px 30px 120px;
    background: linear-gradient(120deg, #3a3430 0%, #6b655e 35%, #d8552c 65%, #2e2925 100%);
    z-index: 1;
  }
  .info-strip {
    position: absolute;
    top: 324px;
    height: 56px;
    display: flex;
    align-items: center;
    z-index: 2;
    white-space: nowrap;
  }
  .info-strip--web {
    left: 20px;
    width: 560px;
    padding-left: 38px;
    background: linear-gradient(90deg, rgba(255,255,255,0) 0%, var(--white) 7%, var(--white) 88%, rgba(255,255,255,0) 100%);
  }
  .info-strip--mail {
    left: 1064px;
    width: 412px;
    padding-left: 28px;
    background: linear-gradient(90deg, rgba(255,255,255,0) 0%, var(--white) 8%, var(--white) 94%, rgba(255,255,255,0.4) 100%);
  }
  .website {
    font-family: "Open Sans", sans-serif;
    font-weight: 700;
    font-size: 26px;
    color: var(--ink);
    letter-spacing: 0.2px;
  }
  .email {
    font-family: "Open Sans", sans-serif;
    font-weight: 600;
    font-size: 15px;
    color: var(--ink);
    letter-spacing: 0.3px;
  }
  .call-block {
    position: absolute;
    left: 1120px;
    top: 52px;
    width: 340px;
    text-align: center;
    z-index: 2;
  }
  .phone-icon {
    display: block;
    margin: 0 auto 18px;
    width: 62px;
    height: 62px;
  }
  .call-now,
  .phone-number {
    font-family: "Anton", "Impact", sans-serif;
    color: var(--orange);
    letter-spacing: 1px;
    line-height: 1;
  }
  .call-now { font-size: 58px; }
  .phone-number { font-size: 50px; margin-top: 8px; }
</style>
</head>
<body>
<main class="canvas">
  <section class="billboard">
    <svg class="billboard-bg" viewBox="0 0 1480 432" aria-hidden="true">
      <rect width="1480" height="432" fill="var(--orange)"/>
      <polygon points="676,0 1480,0 1480,432 900,432" fill="var(--tan)"/>
      <polygon points="806,0 1480,0 1480,432 1030,432" fill="var(--charcoal)"/>
    </svg>

    <h1 class="brand-name">BRASKET<br>LAND<br>SERVICES</h1>

    <div class="loader-photo" role="img" aria-label="Photo of an orange tracked loader with a forestry mulcher attachment"></div>

    <div class="info-strip info-strip--web">
      <span class="website">www.brasketlandservices.example</span>
    </div>

    <div class="info-strip info-strip--mail">
      <span class="email">CONTACT@BRASKETLANDSERVICES.EXAMPLE</span>
    </div>

    <div class="call-block">
      <svg class="phone-icon" viewBox="0 0 62 62" aria-hidden="true">
        <circle cx="31" cy="31" r="29" fill="none" stroke="var(--orange)" stroke-width="2"/>
        <path d="M22 19c1.5-1 3-1 4 .5l2.5 4c.7 1.2.4 2.4-.6 3.2l-1.6 1.2c1 2.6 3.2 4.9 5.8 6l1.3-1.6c.8-1 2-1.3 3.2-.6l4 2.4c1.5.9 1.5 2.5.5 4l-1.6 2.2c-1 1.3-2.6 1.8-4.2 1.3C27 39.5 22.5 35 20.4 27.3c-.4-1.6.1-3.2 1.4-4.2z" fill="var(--orange)"/>
      </svg>
      <p class="call-now">CALL NOW!</p>
      <p class="phone-number">555-284-6170</p>
    </div>
  </section>
</main>
</body>
</html>
```